Crest Porter Website Professional and Crisp Redesign

Hi Teams,
Good evening! I am looking for a Warm Crisp and Professional redesign of my company's website at www.CrestPorter.example. Please google "Valet Trash" also to see the low rent stuff my competition is doing. I have included so much material for you to help your creative minds collaborate with. We use Wordpress now and have a mobile app plug in that is using xmlrpc to communicate back and forth iOS and Android. Swift for iOS and Java for android. Wordpress for the site. Good Luck!
Heres a little test site we fooled around with http://crest.kmorr.example to get ideas flowing, if needed.
Use the new content and redesign file for page content/copy. We all add information like Bio's when we get there.
I want you to be creative - use your own words, just be crisp about it.
Home Page:
Concept:
Nice marsh/tide/palm tree image of a community, poised up to the sky.
Crest porter sign for each of the respective redirections/pages. (4 total)
Statement:
Crest Porter is a leading valet trash and recycling service provider offering robust and flexible solutions for your community’s recycling, waste and maintenance needs. Connect with us and let us give you and your residents the experience they deserve: Better people, better processes, and better technologies.
Video –
Client Login – top left always
Slogan – Improve the day with valet.
Tabs: (Could be in boxes or the Crest Porter sign)
1. Residents
2. Property Management
3. About us
4. Contact
Residents Page:
Dear Resident,
Making sure that our environment and communities stay beautiful is a part of Crest Porter’s mission. We owe it to ourselves to be more thoughtful in our own waste production by ensuring the items we discard have fulfilled their highest and best uses. We are thankful for the steps we take together that propel us in the right direction.
Video.
Why Valet:
Crest Porter solves the embarrassment and effort of handling waste and recycling for the sophisticated multifamily resident. We always like to say – find us one person who likes to take out the trash…
Service guidelines on display and downloadable.
Oops!
Picture of an example oops note –
Get one of these?! No sweat, just correct the checked box the next night and we will happily take your trash/recycling the next scheduled service evening.
Essentials:
1. Trash is tied, bagged, and in the provided container.
(max 2 bags, 25 lbs/night)
2. Ensure bins are placed and returned at the agreed upon times.
3. Always feel free to contact us with any questions, comments, or concerns.
Management Page
Dear Management,
As our multifamily industry grows and continues to evolve with our residents, add value industries like Valet Trash are emerging as best bets for better serving your community as a whole. Knowing the industry as we do, Crest Porter knows that how we perform in New York, directly impacts our teams opportunities in Florida. By instilling this united culture we are consistently able to outperform our industry’s key performance indicators such as retention rate that affords Crest Porter the advantage in most cases.
Video:
Why Crest?
1. Our Values –
Integrity | We are transparent and forthright in what we do.
Outstanding Customer Service | For us this means doing more than just what we are compensated for.
Accountability | In our industry, it’s the one miss that is remembered, so we always have redundancy plans and the technology needed to keep our clients well rested.
Strong Work Ethic | Discipline is the cornerstone of great results, and reliability.
2. Our People –
Crest Porter hosts tryouts, not interviews for all its thoroughly background checked employees. Tryouts ensure our high standards of integrity, accountability, and strong work ethics are consistently observed before allowing them on-site alone.
3. Our Process –
Our employee’s are trained to be safe problem solvers from the start. We take a 500-foot view above the job scope to develop safer, more efficient, and through ways of improving our work and culture. Then, we listen.
4. Our Technology –
Technology has allowed Crest Porter to better bridge the communication gap for our clients to get on-site performance data real time. Our application, H2H (Hall to hall), allows fast accurate reporting of our job assignments. This tool takes out the guesswork and follow up time when we have inquires.
5. Our Dividends –
No need to budget when our service generates profit infinitely with no start up investment through our phase in programs. We will always consider buying out the current provider’s contract as requested.
6. Our Involvements –
A chief aim for Crest Porter is to uplift and connect with our teammates, our clients, and our communities. We always find brilliant ways to contribute both with micro and macro impacts consistently. Check the attendance records of your local and national meetings and events – you’ll see that we show up. We are committed.
Connect with us to inquire more information and pricing
Info@CrestPorter.example | 885- CRST-PQL
Download information package
About
Hi There,
After spilling leaking trash in a brand new car on the way to the community compactor, enough was enough. The company was formed that same evening and the founder turned in his safe executive roll for a fortune 500 company and dove into the world of the unknown – Entrepreneurship. Through the merits of our service, self-investment, and teach-ability index Crest Porter is fast becoming a stable leader in setting the standard for valet trash.
Video
Leadership
Executive Team
Ray Fenwick
Glen Matusiak
Tara Hollins
Marla Quenvick
Ingrid Falkner
Area Management
New York
South Carolina
North Carolina
Georgia
Florida
Louisiana
Alabama
Texas
Contact page:
Pretty straight forward.
Again Good Luck!
Ray Fenwick
President
Crest Porter
Target Market(s)
Professionals
Industry/Entity Type
Apartment
Number of Pages Required
5+ page
Font styles to use
Requirements
Must have
- Professional, Organized, and Crisp
Nice to have
- You go out on your own and put your own touch on it. That would be refreshing.
Should not have
- Don't use the word "Complex" to talk about apartments. Have fun!

```html
<!DOCTYPE html>
<html lang="en">
<head>
<meta charset="utf-8">
<title>Crest Porter — Valet Waste Management Services</title>
<link href="https://fonts.googleapis.com/css2?family=Source+Sans+3:wght@400;600;700&display=swap" rel="stylesheet">
<style>
:root{
  --brand:#1f6fb2;
  --ink:#222;
  --body:#555;
  --muted:#777;
  --sky:#7ec8ea;
  --card-blue:#d2e9f6;
  --card-art:#c3e0f1;
  --band-mint:#d3ebe6;
  --band-blue:#cce5f2;
  --tab-blue:#a9d6ef;
  --tab-mint:#a8dccf;
  --tab-steel:#b3cde6;
  --line:#e2e2e2;
  --white:#fff;
}
*{box-sizing:border-box;margin:0;padding:0}
html,body{width:1200px;height:2597px;overflow:hidden}
body{position:relative;background:var(--white);font-family:"Source Sans 3",Arial,sans-serif;color:var(--ink)}
.abs{position:absolute}

/* header */
.site-header{left:0;top:0;width:1200px;height:78px;background:var(--white)}
.brand{display:flex;align-items:center;gap:8px}
.brand-mark{width:34px;height:34px;border-radius:50%;background:var(--brand)}
.brand-name{font-size:38px;font-weight:700;color:var(--brand);line-height:1}
.brand-tag{font-size:10px;color:var(--muted);margin-left:42px;margin-top:-2px}
.site-header .brand-wrap{left:111px;top:12px}
.main-nav{left:421px;top:29px;display:flex;gap:23px;font-size:14px;font-weight:600;color:#333;letter-spacing:.2px}
.nav-phone{display:flex;align-items:center;gap:5px}
.btn-login{left:980px;top:21px;width:108px;height:34px;background:var(--sky);color:var(--white);font-size:13px;font-weight:700;display:flex;align-items:center;justify-content:center;border-radius:2px}

/* hero */
.hero{left:0;top:78px;width:1200px;height:514px;background:linear-gradient(180deg,#2a1a10 0%,#b8521c 30%,#e88a2a 45%,#c4561a 55%,#3a2416 75%,#1a120d 100%)}
.hero-title{left:0;top:268px;width:1200px;text-align:center;color:var(--white);font-size:31px;font-weight:700;letter-spacing:.3px}
.hero-text{left:285px;top:306px;width:630px;text-align:center;color:var(--white);font-size:13.5px;line-height:20.5px}
.btn-light{background:var(--white);color:#222;font-size:13px;font-weight:700;display:flex;align-items:center;justify-content:center;border-radius:3px;letter-spacing:.3px}
.hero .btn-light{left:539px;top:391px;width:122px;height:33px}
.hero-dots{left:552px;top:492px;display:flex;gap:8px}
.hero-dots span{width:26px;height:3px;background:rgba(255,255,255,.5)}
.hero-dots span:first-child{background:var(--white)}

/* procedure */
.section-title{width:1200px;left:0;text-align:center;font-size:21px;font-weight:700;color:#222}
.section-sub{width:1200px;left:0;text-align:center;font-size:14px;color:var(--muted)}
.step-card{top:719px;width:308px;height:439px;background:var(--card-blue)}
.step-art{left:0;top:0;width:308px;height:256px;background:var(--card-art)}
.step-rule{left:0;top:256px;width:308px;height:2px;background:#b9dcef}
.step-badge{left:111px;top:256px}
.step-badge span{position:absolute;left:0;top:6px;width:86px;text-align:center;color:var(--white);font-size:13px;font-weight:700}
.step-name{left:0;top:323px;width:308px;text-align:center;font-size:16px;font-weight:600;color:#222;letter-spacing:.3px}
.step-text{left:44px;top:351px;width:220px;text-align:center;font-size:13px;line-height:21px;color:var(--body)}

/* history */
.history-band{left:0;top:1255px;width:1200px;height:355px;background:var(--band-mint)}
.history-title{left:111px;top:1302px;font-size:21px;font-weight:700}
.history-text{left:111px;top:1341px;width:300px;font-size:13px;line-height:20.5px;color:#444}
.history-btn{left:111px;top:1527px;width:123px;height:33px}
.video-frame{left:454px;top:1221px;width:627px;height:332px;background:linear-gradient(135deg,#cfc7bd 0%,#8f8478 45%,#5e4a40 100%);box-shadow:0 3px 8px rgba(0,0,0,.15)}
.video-play{left:287px;top:140px}

/* difference */
.value-item{top:1713px;width:140px;text-align:center}
.value-ring{width:110px;height:110px;border-radius:50%;border:2px solid #c3e2f3;margin:0 auto;display:flex;align-items:center;justify-content:center}
.value-label{margin-top:17px;font-size:15px;font-weight:600;line-height:15px;color:#333;letter-spacing:.4px}

/* features */
.feature-band{left:0;top:1913px;width:1200px;height:477px;background:var(--band-blue)}
.feature-card{top:1964px;width:308px;height:372px;background:var(--white);box-shadow:0 1px 3px rgba(0,0,0,.08)}
.feature-photo{left:0;top:0;width:308px;height:206px}
.feature-name{left:0;top:228px;width:308px;text-align:center;font-size:16px;font-weight:600;letter-spacing:.3px}
.feature-text{left:40px;top:256px;width:228px;text-align:center;font-size:13px;line-height:21px;color:var(--body)}
.tab-more{left:96px;top:337px;width:116px;height:35px;border-radius:14px 14px 0 0;color:var(--white);font-size:12px;font-weight:700;display:flex;align-items:center;justify-content:center;letter-spacing:.3px}

/* footer */
.footer-col{top:2422px;font-size:12.5px;line-height:21px;color:#444}
.footer-col h4{font-size:12.5px;font-weight:700;color:#222;margin-bottom:8px;letter-spacing:.3px}
.social{display:flex;gap:6px;margin-top:2px}
.social span{width:28px;height:28px;border-radius:50%;border:1.5px solid #999}
.footer-brand{left:866px;top:2420px}
.footer-brand .brand-name{font-size:34px}
.footer-brand .brand-mark{width:30px;height:30px}
.footer-legal{left:700px;top:2496px;width:388px;text-align:right;font-size:12.5px;line-height:20px;color:#444}
</style>
</head>
<body>

<header class="abs site-header">
  <div class="abs brand-wrap">
    <div class="brand"><span class="brand-mark"></span><span class="brand-name">Crest Porter</span></div>
    <div class="brand-tag">Valet Waste Management Services</div>
  </div>
  <nav class="abs main-nav">
    <span>RESIDENTS</span><span>PROPERTY MANAGEMENT</span><span>ABOUT US</span><span>CONTACT</span>
    <span class="nav-phone"><svg width="9" height="14" viewBox="0 0 9 14"><rect x="0.5" y="0.5" width="8" height="13" rx="1.5" fill="#7ec8ea"/><rect x="2" y="2.5" width="5" height="7" fill="#fff"/></svg>885- CRST-PQL</span>
  </nav>
  <div class="abs btn-login">CLIENT LOGIN</div>
</header>

<section class="abs hero" role="img" aria-label="Sunset over a lake with silhouetted pine trees">
  <h1 class="abs hero-title">IMPROVE THE DAY WITH VALET</h1>
  <p class="abs hero-text">Crest Porter is aleading valet trash and recycling service provider offering robust and flexible solutions for your community's recycling, waste and maintenance needs.&nbsp; Connect with us and let us give you and your residents the experience they deserve: Better people, better processes, and better technologies.</p>
  <div class="abs btn-light">EXPLORE MORE</div>
  <div class="abs hero-dots"><span></span><span></span><span></span></div>
</section>

<h2 class="abs section-title" style="top:637px">CRESTPORTER PROCEDURE</h2>
<p class="abs section-sub" style="top:665px">Doorside Trash Pickup</p>

<article class="abs step-card" style="left:111px">
  <div class="abs step-art" role="img" aria-label="Illustration of a trash bin placed beside an apartment door under a clock"></div>
  <div class="abs step-rule"></div>
  <div class="abs step-badge"><svg width="86" height="40" viewBox="0 0 86 40"><polygon points="0,0 86,0 43,40" fill="#7ec8ea"/></svg><span>01</span></div>
  <h3 class="abs step-name">PLACEMENT</h3>
  <p class="abs step-text">Mauris in erat justo. Nullam ac urna eu felis dapibus condimentum sit amet a augue. Sed non neque elit.</p>
</article>
<article class="abs step-card" style="left:445px">
  <div class="abs step-art" role="img" aria-label="Illustration of a valet collecting trash from an apartment building under a clock"></div>
  <div class="abs step-rule"></div>
  <div class="abs step-badge"><svg width="86" height="40" viewBox="0 0 86 40"><polygon points="0,0 86,0 43,40" fill="#7ec8ea"/></svg><span>02</span></div>
  <h3 class="abs step-name">PICKUP</h3>
  <p class="abs step-text">Mauris in erat justo. Nullam ac urna eu felis dapibus condimentum sit amet a augue. Sed non neque elit.</p>
</article>
<article class="abs step-card" style="left:779px">
  <div class="abs step-art" role="img" aria-label="Illustration of an empty bin returned to an apartment door under a clock"></div>
  <div class="abs step-rule"></div>
  <div class="abs step-badge"><svg width="86" height="40" viewBox="0 0 86 40"><polygon points="0,0 86,0 43,40" fill="#7ec8ea"/></svg><span>03</span></div>
  <h3 class="abs step-name">RETURN</h3>
  <p class="abs step-text">Mauris in erat justo. Nullam ac urna eu felis dapibus condimentum sit amet a augue. Sed non neque elit.</p>
</article>

<section class="abs history-band"></section>
<h2 class="abs history-title">COMPANY HISTORY</h2>
<p class="abs history-text">The company traces its roots to an unfortunate situation involving spilled trash in a new car. While heading to work with a trash bag riding shotgun, the short ride ended with spilled trash and permanent stains in the owner's new car. The company was formed that very evening when it was decided there must be a better alternative to carrying trash down flights of stairs.</p>
<div class="abs btn-light history-btn">EXPLORE MORE</div>
<div class="abs video-frame" role="img" aria-label="Company introduction video showing a presenter at a desk with a laptop">
  <svg class="abs video-play" width="54" height="54" viewBox="0 0 54 54"><circle cx="27" cy="27" r="27" fill="rgba(0,0,0,.55)"/><polygon points="21,16 21,38 39,27" fill="#fff"/></svg>
</div>

<h2 class="abs section-title" style="top:1657px">WHAT MAKES THE DIFFERENCE?</h2>

<div class="abs value-item" style="left:112px">
  <div class="value-ring"><svg width="50" height="50" viewBox="0 0 50 50" fill="none" stroke="#111" stroke-width="2"><polygon points="12,10 38,10 46,20 25,44 4,20"/><path d="M4 20h42M18 10l-4 10 11 24 11-24-4-10M25 10l-7 10M25 10l7 10"/></svg></div>
  <div class="value-label">OUR<br>VALUES</div>
</div>
<div class="abs value-item" style="left:280px">
  <div class="value-ring"><svg width="50" height="50" viewBox="0 0 50 50" fill="none" stroke="#111" stroke-width="2"><circle cx="13" cy="12" r="5"/><circle cx="25" cy="10" r="5"/><circle cx="37" cy="12" r="5"/><path d="M7 44V22h12v22M19 42V19h12v23M31 44V22h12v22"/></svg></div>
  <div class="value-label">OUR<br>PEOPLE</div>
</div>
<div class="abs value-item" style="left:446px">
  <div class="value-ring"><svg width="50" height="50" viewBox="0 0 50 50" fill="none" stroke="#111" stroke-width="2"><circle cx="25" cy="25" r="14"/><circle cx="25" cy="25" r="8"/><path d="M25 5v6M25 39v6M5 25h6M39 25h6M11 11l4 4M35 35l4 4M39 11l-4 4M15 35l-4 4"/></svg></div>
  <div class="value-label">OUR<br>PROCESS</div>
</div>
<div class="abs value-item" style="left:614px">
  <div class="value-ring"><svg width="50" height="50" viewBox="0 0 50 50" fill="none" stroke="#111" stroke-width="2"><path d="M18 34c0-6-6-9-6-16a13 13 0 0 1 26 0c0 7-6 10-6 16z"/><path d="M19 38h12M20 42h10M25 1v4M8 8l3 3M42 8l-3 3M3 20h4M43 20h4"/></svg></div>
  <div class="value-label">OUR<br>TECHNOLOGY</div>
</div>
<div class="abs value-item" style="left:780px">
  <div class="value-ring"><svg width="54" height="50" viewBox="0 0 54 50" fill="none" stroke="#111" stroke-width="2"><rect x="3" y="12" width="44" height="24"/><rect x="7" y="16" width="44" height="24"/><circle cx="29" cy="28" r="7"/><path d="M29 24v8"/></svg></div>
  <div class="value-label">OUR<br>DIVIDENDS</div>
</div>
<div class="abs value-item" style="left:948px">
  <div class="value-ring"><svg width="54" height="50" viewBox="0 0 54 50" fill="none" stroke="#111" stroke-width="2"><path d="M3 18l10-6 8 4 8-4 10 2 12 8-8 10-10-8-6 4-8-4"/><path d="M13 12l-8 14 6 4M23 34l4 4M19 30l4 4M31 36l4 4M35 32l4 4"/></svg></div>
  <div class="value-label">OUR<br>INVOLVEMENTS</div>
</div>

<section class="abs feature-band"></section>
<article class="abs feature-card" style="left:111px">
  <div class="abs feature-photo" role="img" aria-label="Photo of a modern apartment community with a swimming pool" style="background:linear-gradient(180deg,#9cc6e6 0%,#c9d6de 45%,#8ea0a6 70%,#5fb4cf 100%)"></div>
  <h3 class="abs feature-name">WHO</h3>
  <p class="abs feature-text">Mauris in erat justo. Nullam ac urna eu felis dapibus condimentum sit amet a augue. Sed non neque elit. Sed ut imperdiet nisi.</p>
  <div class="abs tab-more" style="background:var(--tab-blue)">READ MORE</div>
</article>
<article class="abs feature-card" style="left:445px">
  <div class="abs feature-photo" role="img" aria-label="Photo of a valet in a safety vest in front of an apartment building" style="background:linear-gradient(180deg,#8fb7d8 0%,#c7b59c 45%,#7b705f 75%,#3e3a36 100%)"></div>
  <h3 class="abs feature-name">EXPERIENCE</h3>
  <p class="abs feature-text">Mauris in erat justo. Nullam ac urna eu felis dapibus condimentum sit amet a augue. Sed non neque elit. Sed ut imperdiet nisi.</p>
  <div class="abs tab-more" style="background:var(--tab-mint)">READ MORE</div>
</article>
<article class="abs feature-card" style="left:779px">
  <div class="abs feature-photo" role="img" aria-label="Map of the United States highlighting southeastern service states" style="background:#e2e2e2"></div>
  <h3 class="abs feature-name">LOCATIONS</h3>
  <p class="abs feature-text">Mauris in erat justo. Nullam ac urna eu felis dapibus condimentum sit amet a augue. Sed non neque elit. Sed ut imperdiet nisi.</p>
  <div class="abs tab-more" style="background:var(--tab-steel)">READ MORE</div>
</article>

<footer>
  <div class="abs footer-col" style="left:111px">
    <h4>CONTACT INFO</h4>
    Corporate Headquarters<br>418 Harlow Ave. | Suite 300<br>Brightwater, SC 29000<br><br>Toll Free: 1.855.CRST.PQL<br>info@crestporter.example
  </div>
  <div class="abs footer-col" style="left:315px">
    <h4>QUICK LINKS</h4>
    Home<br>Residents<br>Property Management<br>About Us<br>Contact<br>Client Login
  </div>
  <div class="abs footer-col" style="left:483px">
    <h4>COMPANY</h4>
    <div class="social"><span></span><span></span><span></span><span></span><span></span></div>
  </div>
  <div class="abs footer-brand">
    <div class="brand"><span class="brand-mark"></span><span class="brand-name">Crest Porter</span></div>
    <div class="brand-tag" style="margin-left:38px">Valet Waste Management Services</div>
  </div>
  <div class="abs footer-legal">© 2017 CrestPorter. All Rights Reserved<br>Terms of Use | Privacy Policy | Sitemap</div>
</footer>

</body>
</html>
```